Business Card Design

I need a business card that is sleek/professional, I am a hair stylist that is trendy and I want my business cards to fit my style. I would like for them to be black or gray and maybe the print to be white. I also want them to be read easily, I don't want clients to have to squint their eyes to see the print. I want the back of the card to have a space for me to write there next appointment on and maybe a short sentence thanking them for their visit.

Industry/Entity Type

Hair

Contact Information for Business Card

Hair Horizons by Tavio @ Marcus Delane Salons, Owner/Hair Stylist/Makeup Artist-Tavio Ormonde ,Kelmar Method Educator, 4186F Meadow Crest Blvd Ste.302 Sugarland Tx 77512,Phone# 281-555-0246

```html
<!DOCTYPE html>
<html lang="en">
<head>
<meta charset="utf-8">
<title>Hair Horizons by Tavio – Business Card</title>
<link rel="stylesheet" href="https://fonts.googleapis.com/css2?family=Fondamento&display=swap">
<style>
  :root {
    --backdrop: #8e9497;
    --card-black: #0c0907;
    --copper: #b8621d;
    --copper-soft: rgba(184, 98, 29, 0.55);
    --copper-faint: rgba(184, 98, 29, 0.18);
    --parchment: #cbb99e;
    --rule: rgba(203, 185, 158, 0.55);
    --card-shadow: rgba(0, 0, 0, 0.35);
  }
  * { margin: 0; padding: 0; box-sizing: border-box; }
  html, body {
    width: 1200px;
    height: 903px;
    overflow: hidden;
    background: var(--backdrop);
  }
  .sheet {
    position: relative;
    width: 1200px;
    height: 903px;
    display: flex;
    flex-direction: column;
    align-items: center;
    justify-content: center;
    gap: 40px;
  }
  .card {
    position: relative;
    width: 640px;
    height: 366px;
    background: var(--card-black);
    box-shadow: 0 10px 24px var(--card-shadow);
    overflow: hidden;
    font-family: "Fondamento", cursive;
  }
  .flourish {
    position: absolute;
    width: 230px;
    height: 200px;
  }
  .flourish--top-left {
    top: 0;
    left: 0;
    background: radial-gradient(ellipse at 20% 0%, var(--copper-soft) 0%, var(--copper-faint) 40%, transparent 72%);
  }
  .flourish--bottom-right {
    bottom: 0;
    right: 0;
    background: radial-gradient(ellipse at 90% 100%, var(--copper-soft) 0%, var(--copper-faint) 40%, transparent 72%);
  }
  .card-text { position: absolute; white-space: nowrap; }

  /* Front */
  .stylist-name {
    top: 34px;
    right: 40px;
    font-size: 24px;
    color: var(--copper);
  }
  .business-name {
    top: 120px;
    left: 120px;
    font-size: 40px;
    font-weight: 400;
    color: var(--parchment);
  }
  .salon-name {
    top: 182px;
    left: 250px;
    font-size: 28px;
    color: var(--copper);
  }

  /* Back */
  .details {
    top: 40px;
    right: 40px;
    text-align: right;
    font-size: 24px;
    line-height: 1.4;
  }
  .details .accent { color: var(--copper); }
  .details .plain { color: var(--parchment); }

  .appointment {
    position: absolute;
    left: 40px;
    bottom: 28px;
    width: 330px;
  }
  .appointment-label {
    font-size: 19px;
    color: var(--copper);
  }
  .appointment-line {
    height: 30px;
    border-bottom: 1px solid var(--rule);
    margin-bottom: 14px;
  }
  .thank-you {
    font-size: 18px;
    color: var(--parchment);
  }
</style>
</head>
<body>
  <main class="sheet">
    <section class="card card--front" aria-label="Card front">
      <div class="flourish flourish--top-left" role="img" aria-label="Copper hair-swirl flourish"></div>
      <div class="flourish flourish--bottom-right" role="img" aria-label="Copper hair-swirl flourish"></div>
      <p class="card-text stylist-name">Tavio Ormonde</p>
      <h1 class="card-text business-name">Hair Horizons by Tavio</h1>
      <p class="card-text salon-name">@ Marcus Delane Salons</p>
    </section>

    <section class="card card--back" aria-label="Card back">
      <div class="flourish flourish--top-left" role="img" aria-label="Copper hair-swirl flourish"></div>
      <div class="flourish flourish--bottom-right" role="img" aria-label="Copper hair-swirl flourish"></div>
      <div class="card-text details">
        <p class="accent">Owner/Hair Stylist/Makeup Artist</p>
        <p class="plain">Kelmar Method Educator</p>
        <p class="accent">phone: 281-555-0246</p>
        <p class="plain">4186F Meadow Crest</p>
        <p class="plain">Blvd Ste.302</p>
        <p class="plain">Sugarland Tx 77512</p>
      </div>
      <div class="appointment">
        <p class="appointment-label">Next appointment:</p>
        <div class="appointment-line"></div>
        <p class="thank-you">Thank you for your visit!</p>
      </div>
    </section>
  </main>
</body>
</html>
```